Restaurant needs a vertical banner for fried catfish

Our restaurant is looking for an eye-catching 78.75in. x 36in. vertical physical banner ad for our fried catfish. Photos for the fried catfish will be provided as a reference but we will also accept anything similar to the photo. We will be using the following as our receptacle: https://www.plankoria.example/banner-stand/retractable-banner-stands/
The design must incorporate the following flavor texts:
Fried Catfish
Always Fresh!
Made from Scratch
Hand-cut Fillets
The Best Catfish in Texas
Served with fries, hush puppies, and a 32oz fountain drink
Also available by the pound!
The final design should be creative, professional, and eye-catching for customers.
Updates
Colors
Designer to choose colors to be used in the design.
Requirements
Must have
- We are open to any and all design elements, albeit the 'flavor texts' should not overpower, but complement the fried catfish photo. 'Fried Catfish' can be used in lieu of a main title/logo.
Nice to have
- Transparent or textured backgrounds that can encompass any or all part of the banner such as a cutting board, shadows, abstract, etc to show depth are a plus.
- Use of vectors or objects such as ribbons or shapes to encapsulate the 'flavor texts' are also encouraged.

```html
<!DOCTYPE html>
<html lang="en">
<head>
<meta charset="utf-8">
<title>Fried Catfish – Vertical Banner</title>
<link rel="stylesheet" href="https://fonts.googleapis.com/css2?family=Bebas+Neue&display=swap">
<style>
  :root {
    --stage: #cbc9cd;
    --brick: #ad3a2c;
    --rust: #c45a2f;
    --amber: #dc8d35;
    --plum: #4a1726;
    --plum-deep: #3c1522;
    --white: #ffffff;
  }
  html, body {
    margin: 0;
    width: 1200px;
    height: 1200px;
    overflow: hidden;
    background: var(--stage);
  }
  .canvas {
    width: 1200px;
    height: 1200px;
    display: flex;
    align-items: center;
    justify-content: center;
  }
  .banner {
    width: 504px;
    height: 1100px;
    display: block;
  }
  .title-main {
    font-family: "Bebas Neue", sans-serif;
    font-size: 164px;
    fill: var(--white);
  }
  .title-sub {
    font-family: "Bebas Neue", sans-serif;
    font-size: 107px;
  }
  .flavor-text {
    font-family: "Bebas Neue", sans-serif;
    font-size: 34px;
    fill: var(--white);
  }
</style>
</head>
<body>
<main class="canvas">
  <svg class="banner" viewBox="0 0 606 1323" xmlns="http://www.w3.org/2000/svg" aria-label="Fried catfish vertical banner">
    <defs>
      <linearGradient id="warmBackdrop" x1="0" y1="0" x2="0" y2="1">
        <stop offset="0" stop-color="var(--brick)"/>
        <stop offset="0.22" stop-color="var(--brick)"/>
        <stop offset="0.4" stop-color="var(--rust)"/>
        <stop offset="0.68" stop-color="var(--amber)"/>
      </linearGradient>
      <linearGradient id="titleInk" x1="0" y1="0" x2="0" y2="1">
        <stop offset="0" stop-color="var(--brick)"/>
        <stop offset="1" stop-color="#d1742f"/>
      </linearGradient>
      <radialGradient id="platePhoto" cx="0.5" cy="0.5" r="0.5">
        <stop offset="0" stop-color="#d99a3e"/>
        <stop offset="0.55" stop-color="#e9c27a"/>
        <stop offset="1" stop-color="#ffffff"/>
      </radialGradient>
      <clipPath id="featureClip">
        <path d="M606 0 L606 618 L340 858 Q313 882 286 856 L58 598 Q36 574 58 550 L606 0 Z"/>
      </clipPath>
    </defs>

    <rect class="backdrop" width="606" height="1323" fill="url(#warmBackdrop)"/>

    <path class="feature-panel" fill="var(--white)"
      d="M606 0 L606 618 L340 858 Q313 882 286 856 L58 598 Q36 574 58 550 L606 0 Z"/>

    <g clip-path="url(#featureClip)">
      <ellipse class="food-photo" role="img" aria-label="Plate of golden fried catfish fillets with fries, lemon and tartar sauce"
        cx="318" cy="655" rx="250" ry="118" fill="url(#platePhoto)"/>
    </g>

    <path class="lower-band" role="img" aria-label="Dark plum lower band"
      fill="var(--plum-deep)" d="M0 803 L606 983 L606 1323 L0 1323 Z"/>
    <path class="base-band" fill="var(--plum)"
      d="M0 878 Q200 885 606 1058 L606 1323 L0 1323 Z"/>
    <rect class="foot-strip" x="0" y="1288" width="606" height="35" fill="var(--plum-deep)"/>

    <text class="title-main" x="38" y="173" textLength="325" lengthAdjust="spacingAndGlyphs">FRIED</text>
    <rect class="title-plate" x="28" y="203" width="378" height="108" fill="var(--white)"/>
    <text class="title-sub" x="41" y="291" textLength="310" lengthAdjust="spacingAndGlyphs" fill="url(#titleInk)">CATFISH</text>

    <g class="flavor-lines" text-anchor="middle">
      <text class="flavor-text" x="299" y="1078" textLength="400" lengthAdjust="spacing">FRIED CATFISH&#160;&#160;&#160;&#160; ALWAYS FRESH!</text>
      <text class="flavor-text" x="291" y="1114" textLength="490" lengthAdjust="spacing">MADE FROM SCRATCH HAND-CUT FILLETS</text>
      <text class="flavor-text" x="305" y="1150" textLength="582" lengthAdjust="spacingAndGlyphs">THE BEST CATFISH IN TEXAS SERVED WITH FRIES,</text>
      <text class="flavor-text" x="308" y="1186" textLength="531" lengthAdjust="spacing">HUSH PUPPIES, AND A 32OZ FOUNTAIN DRINK</text>
      <text class="flavor-text" x="309" y="1222" textLength="386" lengthAdjust="spacing">ALSO AVAILABLE BY THE POUND!</text>
    </g>
  </svg>
</main>
</body>
</html>
```